Building company buisness cards

We are looking for a sharp modern new look for our business cards.
We are a New Zealand based company that specialises in house and land packages.
We have attached a photo of the current logo and would like to see if it can be improved somehow if needed.
We are open to any colours but we have chosen green at this stage.
Feel free to change the font and make the logo smarter looking.
Play with the colours and see what looks best.

We want a card that looks so good know one will want to throw it away!

Target Market(s)

Home buyers

Industry/Entity Type

Building

Contact Information for Business Card

Garth Ellery
0219364028
gellery@tidewaterhomecraft.co.nz
tidewaterhomecraft.co.nz

Font styles to use
Serif
Sans Serif

Colors

Designer to choose colors to be used in the design.

Requirements
Must have
• Logo and company name on one side, details on the other side
Nice to have
• Color codes for the original green are HEX #4a8028, RGB(74,128,40), CMYK(42,0,69,50)
• Round corners, Raised and/or spot UV

```html
<!DOCTYPE html>
<html lang="en">
<head>
<meta charset="utf-8">
<title>Tidewater Homecraft – Business Cards</title>
<link rel="stylesheet" href="https://fonts.googleapis.com/css2?family=Open+Sans:wght@400&display=swap">
<style>
  :root {
    --brand-green: #2f9a1e;
    --card-white: #ffffff;
    --ink: #1c1c1c;
    --stage: #2e2e30;
    --rule: #d6d6d6;
    --photo-roof: #5b5d66;
    --photo-wall: #d8b27a;
    --photo-sky: #cfd4d8;
  }
  html, body {
    margin: 0;
    padding: 0;
    width: 1200px;
    height: 716px;
    overflow: hidden;
    background: var(--stage);
    font-family: "Open Sans", Arial, sans-serif;
  }
  .canvas {
    position: relative;
    width: 1200px;
    height: 716px;
  }
  .card {
    position: absolute;
    top: 208px;
    width: 520px;
    height: 300px;
    background: var(--card-white);
    border-radius: 10px;
    overflow: hidden;
  }
  .card--front { left: 45px; }
  .card--back  { left: 635px; }

  .company-name {
    margin: 0;
    color: var(--brand-green);
    font-weight: 400;
    line-height: 1.2;
    white-space: nowrap;
  }
  .card--front .company-name {
    position: absolute;
    left: 0; right: 0;
    top: 128px;
    font-size: 28px;
    text-align: center;
  }
  .card--front .name-rule {
    position: absolute;
    left: 230px;
    width: 60px;
    top: 184px;
    height: 1px;
    background: var(--rule);
  }

  .card--back .photo {
    position: absolute;
    left: 0; top: 0;
    width: 240px;
    height: 300px;
  }
  .card--back .company-name {
    position: absolute;
    right: 22px;
    top: 104px;
    font-size: 22px;
    text-align: right;
  }
  .contact {
    position: absolute;
    right: 22px;
    top: 178px;
    text-align: right;
    color: var(--ink);
  }
  .contact-name {
    font-size: 17px;
    margin: 0 0 16px 0;
    font-weight: 400;
  }
  .contact-line {
    display: flex;
    justify-content: flex-end;
    align-items: center;
    gap: 8px;
    font-size: 11.5px;
    height: 19px;
  }
  .contact-icon {
    width: 13px;
    height: 13px;
    flex: none;
  }
</style>
</head>
<body>
<main class="canvas">

  <section class="card card--front" aria-label="Card front">
    <p class="company-name">Tidewater Homecraft</p>
    <div class="name-rule"></div>
  </section>

  <section class="card card--back" aria-label="Card back">
    <svg class="photo" viewBox="0 0 240 300" role="img" aria-label="Photo of a model two-storey house with a grey roof and tan walls">
      <defs>
        <linearGradient id="houseTones" x1="0" y1="0" x2="1" y2="1">
          <stop offset="0" stop-color="#cfd4d8"/>
          <stop offset="0.35" stop-color="#5b5d66"/>
          <stop offset="0.7" stop-color="#d8b27a"/>
          <stop offset="1" stop-color="#e9e6e0"/>
        </linearGradient>
      </defs>
      <path d="M0 0 H150 Q240 150 150 300 H0 Z" fill="url(#houseTones)"/>
    </svg>

    <p class="company-name">Tidewater Homecraft</p>

    <div class="contact">
      <p class="contact-name">Garth Ellery</p>
      <div class="contact-line">
        <span>0219364028</span>
        <svg class="contact-icon" viewBox="0 0 13 13" aria-hidden="true">
          <rect width="13" height="13" rx="2" fill="var(--brand-green)"/>
          <path d="M4 3 L5.5 3 L6 5 L5 5.8 Q6 7.6 7.2 8 L8 7 L10 7.5 L10 9 Q6 10 3.5 4.5 Z" fill="#fff"/>
        </svg>
      </div>
      <div class="contact-line">
        <span>gellery@tidewaterhomecraft.co.nz</span>
        <svg class="contact-icon" viewBox="0 0 13 13" aria-hidden="true">
          <rect width="13" height="13" rx="2" fill="var(--brand-green)"/>
          <rect x="3" y="4" width="7" height="5" fill="none" stroke="#fff" stroke-width="1"/>
          <path d="M3 4 L6.5 7 L10 4" fill="none" stroke="#fff" stroke-width="1"/>
        </svg>
      </div>
      <div class="contact-line">
        <span>tidewaterhomecraft.co.nz</span>
        <svg class="contact-icon" viewBox="0 0 13 13" aria-hidden="true">
          <rect width="13" height="13" rx="2" fill="var(--brand-green)"/>
          <circle cx="6.5" cy="6.5" r="3.5" fill="none" stroke="#fff" stroke-width="1"/>
          <path d="M3 6.5 H10 M6.5 3 Q4.8 6.5 6.5 10 M6.5 3 Q8.2 6.5 6.5 10" fill="none" stroke="#fff" stroke-width="0.8"/>
        </svg>
      </div>
    </div>
  </section>

</main>
</body>
</html>
```